Bold Cover needed for a book on Workplace Bullying

I need a book cover design for a book titled, “Quiet Harbour?” The book recounts my story of bullying in the workplace. It also includes chapters on how readers can minimize/stop workplace bullying, write an effective complaint, and ensure their own mental wellbeing.
I am looking for a bold design using red and black, and possibly distressed lettering. The covers of other books dealing with this subject do not reflect my vision. They are often too childish or look too academic. This book needs to stress the serious nature of a toxic workplace, while appealing to readers experiencing a similar situation. I’d like the cover to reflect the mental anguish associated with workplace bullying (hence the distressed lettering).
I have included a cover that appeals to me (although the coloring is wrong). That said, I am also very happy (and excited) to see your creative input!
On the cover, it should have the following:
Title: Quiet Harbour?
Subtitle: How the Transit Department Condones Bullying & Ruins Lives
Author: Owen Petrick
Other relevant details:
Book size: 5.5” x 8.5”
Back cover will have a blurb, author picture/short bio, and barcode
The blurb on the back cover reads:
Undermining, intimidation and threats
Despite the Department of Transit allegedly holding a zero tolerance for bullying, these behaviours were an everyday occurrence in at least one workplace. Even after a decade of complaints, numerous witnesses and physical proof, the department failed to act. Instead, they looked the other way, allowing one powerful and well-connected individual to end careers and ruin lives.
After being targeted, one teacher resolved to put an end to the abuse experienced by more than fifty employees. His startling story reveals the relentless bullying, mental health ramifications, and insidious tactics used to cover up the corrosive behaviour.
Those who have experienced a toxic workplace will also find much needed support and guidance, intended to minimise suffering and detail a clear way forward. Chapters include dealing with bullying in the workplace, how to lodge a successful complaint, and how to stay sane during any potential legal action.

```html
<!DOCTYPE html>
<html lang="en">
<head>
<meta charset="utf-8">
<title>Quiet Harbour? — Book Cover</title>
<link rel="stylesheet" href="https://fonts.googleapis.com/css2?family=Anton&family=Russo+One&family=Archivo:wght@700&display=swap">
<style>
  :root {
    --page: #ffffff;
    --cover: #050505;
    --stone-light: #e6e6e1;
    --stone-mid: #c2c2bd;
    --stone-dark: #93938f;
    --accent: #d8261c;
  }
  html, body {
    margin: 0;
    width: 1200px;
    height: 1200px;
    overflow: hidden;
    background: var(--page);
  }
  .canvas { display: block; width: 1200px; height: 1200px; }
  .cover-board { fill: var(--cover); }
  .title-word {
    font-family: "Anton", "Bebas Neue", sans-serif;
    fill: url(#stoneFill);
    filter: url(#distress);
  }
  .subtitle-line {
    font-family: "Archivo", Arial, sans-serif;
    font-weight: 700;
    font-size: 26px;
    fill: var(--accent);
    letter-spacing: 0.5px;
  }
  .author-name {
    font-family: "Russo One", sans-serif;
    fill: var(--accent);
    filter: url(#grain);
  }
</style>
</head>
<body>
<svg class="canvas" viewBox="0 0 1200 1200" xmlns="http://www.w3.org/2000/svg" role="img" aria-label="Book cover: Quiet Harbour? How the Transit Department condones bullying and ruins lives, by Owen Petrick">
  <defs>
    <linearGradient id="stoneFill" x1="0" y1="0" x2="1" y2="1">
      <stop offset="0" stop-color="#e6e6e1"/>
      <stop offset="0.5" stop-color="#c2c2bd"/>
      <stop offset="1" stop-color="#93938f"/>
    </linearGradient>
    <clipPath id="coverClip">
      <rect x="230" y="40" width="740" height="1110"/>
    </clipPath>
    <filter id="distress" x="-2%" y="-2%" width="104%" height="104%">
      <feTurbulence type="fractalNoise" baseFrequency="0.03 0.012" numOctaves="3" seed="7" result="noise"/>
      <feColorMatrix in="noise" type="matrix" values="0 0 0 0 0  0 0 0 0 0  0 0 0 0 0  0 0 0 -10 6.6" result="holes"/>
      <feComposite in="SourceGraphic" in2="holes" operator="in" result="cut"/>
      <feTurbulence type="fractalNoise" baseFrequency="0.06" numOctaves="2" seed="3" result="stain"/>
      <feColorMatrix in="stain" type="matrix" values="0 0 0 0 0.3  0 0 0 0 0.3  0 0 0 0 0.29  0 0 0 -2.4 1.15" result="stainTone"/>
      <feComposite in="stainTone" in2="cut" operator="in" result="stainOnText"/>
      <feMerge><feMergeNode in="cut"/><feMergeNode in="stainOnText"/></feMerge>
    </filter>
    <filter id="grain" x="0" y="0" width="100%" height="100%">
      <feTurbulence type="fractalNoise" baseFrequency="0.6" numOctaves="1" seed="2" result="n"/>
      <feColorMatrix in="n" type="matrix" values="0 0 0 0 0  0 0 0 0 0  0 0 0 0 0  0 0 0 -6 4.6" result="specks"/>
      <feComposite in="SourceGraphic" in2="specks" operator="in"/>
    </filter>
  </defs>

  <rect class="cover-board" x="230" y="40" width="740" height="1110"/>

  <g class="cover-content" clip-path="url(#coverClip)">
    <text class="title-word title-word--top" x="262" y="490" font-size="430" textLength="672" lengthAdjust="spacingAndGlyphs">QUIET</text>

    <text class="subtitle-line" x="600" y="586" text-anchor="middle">HOW THE TRANSIT DEPARTMENT</text>
    <text class="subtitle-line" x="600" y="627" text-anchor="middle">CONDONES BULLYING AND RUINS LIVES</text>

    <text class="title-word title-word--bottom" x="270" y="845" font-size="182" textLength="665" lengthAdjust="spacingAndGlyphs">HARBOUR?</text>

    <text class="author-name" x="440" y="990" font-size="92" textLength="320" lengthAdjust="spacingAndGlyphs">OWEN</text>
    <text class="author-name" x="358" y="1073" font-size="92" textLength="482" lengthAdjust="spacingAndGlyphs">PETRICK</text>
  </g>
</svg>
</body>
</html>
```